Walk Beside The River

Business Card design

Target Market(s)

People who require support in the commnity

Industry/Entity Type

Mental Health Support

Contact Information for Business Card

Mental Health Support Rosalind Tavener walkbesidetheriver@mailbrook.com.au 0458 906 312 PO Box 627 Wattlemere QLD 4599

Colors
6B429C
8869AF
B7A5CE
E3DAEB
F3F0F8

Requirements
Must have
• Logo & details listed above
Should not have
• No red or orange

```html
<!DOCTYPE html>
<html lang="en">
<head>
<meta charset="utf-8">
<title>Walk Beside The River – Business Card</title>
<link rel="stylesheet" href="https://fonts.googleapis.com/css2?family=Lato:wght@400;700;900&display=swap">
<style>
  :root {
    --stage: #7f9cbd;
    --card-white: #f4f4f6;
    --sun-yellow: #f2ec2a;
    --purple-deep: #6b429c;
    --purple-mid: #8869af;
    --ink: #222226;
    --ink-soft: #3a3a40;
  }
  * { box-sizing: border-box; margin: 0; padding: 0; }
  html, body {
    width: 1200px; height: 876px; overflow: hidden;
    background: var(--stage);
    font-family: "Lato", Arial, sans-serif;
  }
  .sheet {
    position: relative; width: 1200px; height: 876px;
    display: flex; flex-direction: column; align-items: center; justify-content: center; gap: 50px;
  }
  .card {
    position: relative; width: 600px; height: 343px; overflow: hidden;
    box-shadow: 0 6px 18px rgba(30, 45, 80, 0.25);
  }

  /* Shared brand badge: plain circle with the name set inside */
  .brand-mark {
    border-radius: 50%;
    background: var(--purple-deep);
    display: flex; align-items: center; justify-content: center;
    text-align: center;
  }
  .brand-name {
    font-weight: 700; color: var(--sun-yellow);
    text-transform: uppercase; letter-spacing: 0.12em; line-height: 1.35;
  }

  /* Front */
  .card--front { background: var(--card-white); }
  .front__band {
    position: absolute; left: 95px; top: 0; width: 120px; height: 100%;
    background: var(--sun-yellow);
  }
  .card--front .brand-mark {
    position: absolute; left: 57px; top: 62px;
    width: 196px; height: 196px;
    border: 8px solid var(--card-white);
  }
  .card--front .brand-name { font-size: 15px; width: 140px; }

  .details {
    position: absolute; left: 284px; top: 100px; width: 300px;
  }
  .details__role {
    font-weight: 900; font-size: 17px; color: var(--ink); letter-spacing: 0.01em;
  }
  .details__name {
    font-weight: 700; font-size: 29px; line-height: 1.1; color: var(--purple-deep);
    text-transform: uppercase; white-space: nowrap; margin-bottom: 12px;
  }
  .contact { list-style: none; }
  .contact__item {
    display: flex; align-items: center; gap: 8px;
    font-size: 13.5px; color: var(--ink-soft); line-height: 1.75; white-space: nowrap;
  }
  .contact__icon { width: 12px; height: 12px; flex: none; fill: var(--purple-mid); }

  /* Back */
  .card--back {
    background: var(--sun-yellow);
    display: flex; align-items: center; justify-content: center;
  }
  .card--back .brand-mark { width: 230px; height: 230px; }
  .card--back .brand-name { font-size: 17px; width: 160px; }
</style>
</head>
<body>
<main class="sheet">

  <section class="card card--front" aria-label="Business card front">
    <div class="front__band"></div>
    <div class="brand-mark">
      <p class="brand-name">Walk Beside The River</p>
    </div>

    <div class="details">
      <p class="details__role">MENTAL HEALTH SUPPORT</p>
      <h1 class="details__name">Rosalind Tavener</h1>
      <ul class="contact">
        <li class="contact__item">
          <svg class="contact__icon" viewBox="0 0 12 12" aria-hidden="true"><path d="M6 0a4 4 0 0 0-4 4c0 3 4 8 4 8s4-5 4-8a4 4 0 0 0-4-4zm0 5.6A1.6 1.6 0 1 1 6 2.4a1.6 1.6 0 0 1 0 3.2z"/></svg>
          PO Box 627 Wattlemere QLD 4599
        </li>
        <li class="contact__item">
          <svg class="contact__icon" viewBox="0 0 12 12" aria-hidden="true"><path d="M2.4 0.5 4.2 0l1.1 2.8-1.3 1a6.5 6.5 0 0 0 4.2 4.2l1-1.3L12 7.8l-.5 1.8C11.2 11 10 12 8.6 11.6 4.5 10.5 1.5 7.5.4 3.4 0 2 1 .8 2.4.5z"/></svg>
          0458 906 312
        </li>
        <li class="contact__item">
          <svg class="contact__icon" viewBox="0 0 12 12" aria-hidden="true"><path d="M0 2h12v8H0z M0.8 2.6 6 6.8l5.2-4.2" stroke="#f4f4f6" stroke-width="0.9"/></svg>
          walkbesidetheriver@mailbrook.com.au
        </li>
      </ul>
    </div>
  </section>

  <section class="card card--back" aria-label="Business card back">
    <div class="brand-mark">
      <p class="brand-name">Walk Beside The River</p>
    </div>
  </section>

</main>
</body>
</html>
```